Homes, Invest in Non-performing loans

We need only 3 web pages, one for the home, one for the content, one for the properties.
The main focus of our business is to offer non performing loans (before foreclosures) to the general public. All the non-performing mortgages will end in a house, an apartment, a store, etc.
Our customers are able to invest from 10,000usd to 1,000,000usd (average 50,000usd).
Our customers' usual focus groups are employees who want second earnings, perceiving the business feeling without outlay time. They look for a solid finance sense corporation that confers them certainty.
Nearly all our clients desire the house, apartment, store, etc. more than the actual earnings.
The name of our company is BRAMLEY
Reason: We value the time and effort you already invest in our project. We realize that we did't come back on some of the doubts requested by the designers. It will be inequitable to the designers who prerequisite our feedback. We also appreciate the comprehension of the community in this postponement.
Reason: Designers,
We really apreciate all the time and effort you put on our project. From the begining we ask for 3 pages, so now we will leave the 10 finalist and provide some extra time to submit the other 2 pages.
We will race the price in 10%
Target Market(s)
Our customers average investors works as employees and want to have a second income or business without spending time. (People from 35 to 50)
Industry/Entity Type
Finance
Requirements
Should not have
- FLASH

```html
<!DOCTYPE html>
<html lang="en">
<head>
<meta charset="utf-8">
<title>BRAMLEY – Invest in Non-performing Loans</title>
<link href="https://fonts.googleapis.com/css2?family=Ultra&family=Michroma&family=Ubuntu:wght@400;500&family=Open+Sans:wght@400;600&display=swap" rel="stylesheet">
<style>
:root{
  --navy:#0b1444;
  --navy-deep:#060d33;
  --olive:#7f7a27;
  --gold:#9b982d;
  --ink:#222222;
  --beige:#ece7d6;
  --beige-line:#ddd6bf;
  --rule:#c9c9c9;
  --page:#f1f1f1;
  --white:#ffffff;
  --muted:#7d7a6a;
}
*{box-sizing:border-box;margin:0;padding:0}
html,body{width:1167px;height:1200px;overflow:hidden}
body{position:relative;background:var(--page);font-family:Arial,Helvetica,sans-serif;color:var(--ink)}
.abs{position:absolute}
.slab{font-family:"Ultra",Georgia,serif;font-weight:400;letter-spacing:1px}
.topbar{left:0;top:0;width:1167px;height:4px;background:#3a3a3a}
.header{left:0;top:4px;width:1167px;height:235px;background:var(--white)}
.header-shape{left:0;top:4px}
.gray-rule{left:0;top:239px;width:1167px;height:5px;background:#b9b9b9}
.navy-band{left:0;top:244px;width:1167px;height:259px;background:linear-gradient(180deg,var(--navy-deep),var(--navy))}
.brand{left:152px;top:64px;display:flex;align-items:center;gap:8px}
.brand-mark{width:22px;height:22px;background:var(--olive)}
.brand-name{font-family:"Ultra",Georgia,serif;font-size:30px;color:#2b2b2b}
.nav{left:440px;top:30px;display:flex;font-family:"Michroma",sans-serif;font-size:10px;letter-spacing:1.5px;text-transform:uppercase}
.nav a{color:var(--ink);text-decoration:none;position:absolute;white-space:nowrap}
.home-tab{left:440px;top:4px;width:45px;height:23px;background:#4a4a4a}
.headline{left:415px;top:86px;font-size:31px;color:#2b2b2b;line-height:1}
.headline .amt{color:var(--gold);font-family:Arial,sans-serif;font-weight:700;font-size:38px}
.headline2{left:536px;top:128px;font-size:31px;color:#1d1d1d;line-height:1}
.headline2 .amt{font-family:Arial,sans-serif;font-weight:700;font-size:38px}
.house-art{left:566px;top:138px;width:474px;height:231px;background:radial-gradient(ellipse at 60% 55%,#c9c3b8 0%,#9a5a45 38%,rgba(11,20,68,0) 70%);border-radius:8px}
.welcome{left:153px;top:258px;font-size:27px;color:var(--white)}
.welcome em{font-style:normal;color:var(--gold)}
.intro{left:153px;top:302px;width:500px;font-size:11px;line-height:13.2px;color:var(--white)}
.intro p+p{margin-top:6px}
.btn-more{left:566px;top:416px;width:92px;height:27px;border:2px solid #d8d49a;border-radius:5px;background:var(--gold);color:var(--white);font-family:"Ultra",serif;font-size:11px;display:flex;align-items:center;justify-content:center;letter-spacing:1px}
.news-label{left:787px;top:396px;font-family:"Open Sans",sans-serif;font-size:18px;color:var(--white);letter-spacing:-.3px}
.signup{left:786px;top:420px;width:254px;height:31px;background:var(--white);border-radius:5px;border:1px solid #d5d5d5;display:flex;align-items:center;justify-content:space-between;padding:0 3px 0 10px;font-family:"Open Sans",sans-serif;font-size:12px;color:#555}
.signup span.btn{background:#1a1a1a;color:var(--white);border-radius:4px;height:25px;width:66px;display:flex;align-items:center;justify-content:center;font-size:11px;letter-spacing:.5px}
.panel{left:128px;top:456px;width:912px;height:640px;background:var(--white);box-shadow:0 0 12px rgba(0,0,0,.15)}
.sec-title{font-size:18px;color:var(--navy);white-space:nowrap}
.sec-title em{font-style:normal;color:var(--gold)}
.rule{height:2px;border-top:1px solid var(--rule);border-bottom:1px solid #e6e6e6}
.pager{left:729px;top:486px;display:flex;gap:6px;font-size:9px;color:var(--navy)}
.pager span{width:11px;height:11px;display:flex;align-items:center;justify-content:center}
.pager .on{background:var(--navy);color:var(--white)}
.card{width:212px;height:152px;background:var(--beige);padding:12px 13px}
.card .ph{width:100%;height:100%}
.ph1{background:linear-gradient(160deg,#6f8a5a,#5b5f66 55%,#3f5a2a)}
.ph2{background:linear-gradient(180deg,#3f73c4 0%,#9fbbe0 35%,#e8e2d6 55%,#4f7a3a)}
.ph3{background:linear-gradient(180deg,#dcdcd6,#b8b2a4 60%,#6a7a4a)}
.ph4{background:linear-gradient(180deg,#bcd8ee,#5a8a3a 45%,#9c6a3a 60%,#7fbf4a)}
.ph5{background:linear-gradient(180deg,#2f6fc0,#e8ecef 45%,#d9dbdc 80%,#8a8a8a)}
.ph6{background:linear-gradient(180deg,#f2f2f2,#8a4a35 50%,#3f6a2a)}
.side-title{font-size:15px;color:var(--navy)}
.box{background:var(--beige);font-family:"Ubuntu",sans-serif;font-size:11px;color:var(--muted)}
.rates{left:807px;top:518px;width:213px;height:103px;padding:8px 6px}
.rates table{width:100%;border-collapse:collapse}
.rates td{height:27px;border-bottom:1px dotted #cfc8b0;padding-left:4px}
.rates tr:last-child td{border-bottom:none}
.ico{display:inline-block;width:10px;height:10px;background:#e8e0b8;border:1px solid #b3a86a;margin-right:5px;vertical-align:-1px}
.news{left:807px;top:668px;width:213px;height:165px;padding:10px 6px}
.news li{list-style:none;height:20.5px;display:flex;align-items:center;white-space:nowrap}
.news li svg{margin-right:6px;flex:none}
.feature-box{width:280px;height:184px;border:1px solid #dcdcdc;background:#f6f6f6;padding:11px 13px}
.feature-box .ph{width:100%;height:100%}
.ph-advice{background:linear-gradient(120deg,#e9dccd,#c3ccd6 50%,#f3f3f3)}
.ph-mortgage{background:linear-gradient(180deg,#6a3a2a,#c9b79a 40%,#e9e4d6 60%,#4f8a2f)}
.quote{left:740px;top:862px;width:276px;height:205px;background:var(--olive);border:1px solid #6a661e}
.quote-head{position:absolute;left:17px;top:5px;display:flex;align-items:center;gap:10px;font-family:"Open Sans",sans-serif;font-size:19px;color:var(--white)}
.quote-field{position:absolute;left:16px;width:240px;background:var(--white);font-family:"Open Sans",sans-serif;font-size:11px;color:#333;padding:6px 12px}
.quote-submit{position:absolute;left:195px;top:178px;width:61px;height:20px;background:#111;color:var(--white);font-family:"Open Sans",sans-serif;font-size:11px;display:flex;align-items:center;justify-content:center}
.footer-shape{left:0;top:1070px}
.foot-links{left:145px;top:1119px;font-size:11px;color:var(--white);white-space:nowrap}
.foot-links span.sep{margin:0 8px}
.foot-copy{left:145px;top:1147px;font-size:11px;line-height:19px;color:var(--white)}
.follow{left:627px;top:1116px;font-family:"Open Sans",sans-serif;font-size:18px;color:var(--white);letter-spacing:-.3px}
.social{left:632px;top:1146px;display:flex;gap:7px}
.social span{width:17px;height:17px;border-radius:50%;background:#9aa0b8}
.foot-brand{left:892px;top:1122px;display:flex;align-items:center;gap:7px}
.foot-brand .brand-mark{width:18px;height:18px}
.foot-brand .brand-name{font-size:22px}
</style>
</head>
<body>
<div class="abs topbar"></div>
<div class="abs header"></div>
<svg class="abs header-shape" width="420" height="236" aria-hidden="true">
  <polygon points="0,0 333,0 392,137 160,235 0,235" fill="#efefef"/>
  <polyline points="333,0 392,137 160,235" fill="none" stroke="#b5b5b5" stroke-width="1.5"/>
</svg>
<div class="abs brand"><span class="brand-mark"></span><span class="brand-name">BRAMLEY</span></div>

<div class="abs home-tab">
  <svg width="45" height="23" aria-hidden="true"><path d="M22.5 6 L30 12 H28 V18 H24.5 V14 H20.5 V18 H17 V12 H15 Z" fill="#fff"/></svg>
</div>
<nav class="abs nav">
  <a style="left:2px">Home</a>
  <a style="left:81px">About Us</a>
  <a style="left:194px">Mortgage Tools</a>
  <a style="left:358px">How it Works</a>
  <a style="left:507px">Contact Us</a>
</nav>

<div class="abs headline slab">Invest From <span class="amt">$10,000</span></div>
<div class="abs headline2 slab">to <span class="amt">$1,000,000</span></div>

<div class="abs gray-rule"></div>
<div class="abs navy-band"></div>
<div class="abs house-art" role="img" aria-label="Illustration of a two-storey house with red tiled roof standing on rolled architectural plans"></div>

<h1 class="abs welcome slab">Welcome To <em>BRAMLEY</em></h1>
<div class="abs intro">
  <p>Lorem ipsum dolor sit amet, consectetuer adipiscing elit, sed diam nonummy nibh euismod tincidunt ut laoreet dolore magna aliquam erat volutpat. Ut wisi enim ad minim veniam, quis nostrud exerci tation ullamcorper suscipit lobortis nisl ut aliquip ex ea commodo consequat. Duis autem vel eum iriure dolor in hendrerit in vulputate velit esse molestie consequat, vel illum dolore eu feugiat nulla facilisis at vero eros et accumsan et iusto odio dignissim qui blandit praesent luptatum zzril delenit augue duis dolore te feugait nulla facilisi.</p>
  <p>Lorem ipsum dolor sit amet, consectetuer adipiscing elit, sed diam nonummy nibh euismod tincidunt ut laoreet dolore magna aliquam erat volutpat. Ut wisi enim ad minim veniam.</p>
</div>
<div class="abs btn-more">Read More</div>

<div class="abs news-label">NEWSLETTER SIGN UP</div>
<div class="abs signup"><span>Email Address</span><span class="btn">SIGN UP</span></div>

<div class="abs panel"></div>

<h2 class="abs sec-title slab" style="left:143px;top:480px">Featured <em>Propeties</em></h2>
<div class="abs rule" style="left:143px;top:502px;width:650px"></div>
<div class="abs pager"><span class="on">1</span><span>2</span><span>3</span><span>4</span><span>5</span></div>

<div class="abs card" style="left:142px;top:518px"><div class="ph ph1" role="img" aria-label="Photo of a two-storey family house with garage, listed for rent"></div></div>
<div class="abs card" style="left:362px;top:518px"><div class="ph ph2" role="img" aria-label="Photo of a white villa with tiled roof and palm trees"></div></div>
<div class="abs card" style="left:582px;top:518px"><div class="ph ph3" role="img" aria-label="Photo of a classic house entrance with wrought iron fence"></div></div>
<div class="abs card" style="left:142px;top:681px"><div class="ph ph4" role="img" aria-label="Photo of a wooden cabin on a green lawn"></div></div>
<div class="abs card" style="left:362px;top:681px"><div class="ph ph5" role="img" aria-label="Photo of a white two-storey house with balcony"></div></div>
<div class="abs card" style="left:582px;top:681px"><div class="ph ph6" role="img" aria-label="Photo of a red brick mansion surrounded by trees"></div></div>

<svg class="abs" style="left:808px;top:478px" width="22" height="22" aria-hidden="true">
  <ellipse cx="11" cy="18" rx="9" ry="3" fill="#c9a43a"/><ellipse cx="11" cy="13" rx="9" ry="3" fill="#d9b44a"/><ellipse cx="13" cy="8" rx="7" ry="3" fill="#e6c45a"/>
</svg>
<h2 class="abs side-title slab" style="left:840px;top:482px">Current Rate</h2>
<div class="abs rule" style="left:807px;top:503px;width:214px"></div>
<div class="abs box rates">
  <table>
    <tr><td><span class="ico"></span>Dolar</td><td>1.5052</td><td>1.5125</td></tr>
    <tr><td><span class="ico"></span>Euro</td><td>2.1687</td><td>2.1807</td></tr>
    <tr><td><span class="ico"></span>Sterlin</td><td>2.4018</td><td>2.4144</td></tr>
  </table>
</div>

<svg class="abs" style="left:808px;top:636px" width="24" height="14" aria-hidden="true">
  <rect x="1" y="1" width="22" height="12" fill="#eee" stroke="#999"/><line x1="4" y1="5" x2="20" y2="5" stroke="#999"/><line x1="4" y1="9" x2="20" y2="9" stroke="#999"/>
</svg>
<h2 class="abs side-title slab" style="left:841px;top:637px">News</h2>
<div class="abs rule" style="left:807px;top:657px;width:214px"></div>
<ul class="abs box news">
  <li><svg width="12" height="12"><rect x="1" y="2" width="9" height="9" fill="#f3eed8" stroke="#a89c5a"/><path d="M3 7 L6 9 L11 1" stroke="#8a7f2a" fill="none" stroke-width="1.5"/></svg>Lorem ipsum dolor sit amet</li>
  <li><svg width="12" height="12"><rect x="1" y="2" width="9" height="9" fill="#f3eed8" stroke="#a89c5a"/><path d="M3 7 L6 9 L11 1" stroke="#8a7f2a" fill="none" stroke-width="1.5"/></svg>Consectetur adipiscing elit</li>
  <li><svg width="12" height="12"><rect x="1" y="2" width="9" height="9" fill="#f3eed8" stroke="#a89c5a"/><path d="M3 7 L6 9 L11 1" stroke="#8a7f2a" fill="none" stroke-width="1.5"/></svg>Suspendisse vitae diam elit</li>
  <li><svg width="12" height="12"><rect x="1" y="2" width="9" height="9" fill="#f3eed8" stroke="#a89c5a"/><path d="M3 7 L6 9 L11 1" stroke="#8a7f2a" fill="none" stroke-width="1.5"/></svg>Quis sollicitudin eros sed id</li>
  <li><svg width="12" height="12"><rect x="1" y="2" width="9" height="9" fill="#f3eed8" stroke="#a89c5a"/><path d="M3 7 L6 9 L11 1" stroke="#8a7f2a" fill="none" stroke-width="1.5"/></svg>Sapien dui morbi facilisis adipiscing</li>
  <li><svg width="12" height="12"><rect x="1" y="2" width="9" height="9" fill="#f3eed8" stroke="#a89c5a"/><path d="M3 7 L6 9 L11 1" stroke="#8a7f2a" fill="none" stroke-width="1.5"/></svg>Mauris a ullamcorper odio</li>
  <li><svg width="12" height="12"><rect x="1" y="2" width="9" height="9" fill="#f3eed8" stroke="#a89c5a"/><path d="M3 7 L6 9 L11 1" stroke="#8a7f2a" fill="none" stroke-width="1.5"/></svg>Elementaum nec</li>
</ul>

<h2 class="abs sec-title slab" style="left:143px;top:855px;color:#2b2b2b">Financial <em>Advice</em></h2>
<div class="abs rule" style="left:143px;top:876px;width:280px"></div>
<div class="abs feature-box" style="left:142px;top:883px"><div class="ph ph-advice" role="img" aria-label="Photo of a couple reviewing documents with a financial advisor"></div></div>

<h2 class="abs sec-title slab" style="left:443px;top:855px;color:#2b2b2b">Mortgage <em>Solution</em></h2>
<div class="abs rule" style="left:443px;top:876px;width:276px"></div>
<div class="abs feature-box" style="left:439px;top:883px"><div class="ph ph-mortgage" role="img" aria-label="Photo of a family playing in the front garden of their home"></div></div>

<div class="abs quote">
  <div class="quote-head">
    <svg width="34" height="34" aria-hidden="true"><circle cx="17" cy="17" r="16" fill="#cfeff6"/><circle cx="17" cy="17" r="12" fill="#33b8d6"/><path d="M12 10 H19 L23 14 V24 H12 Z" fill="none" stroke="#fff" stroke-width="1.6"/><line x1="15" y1="17" x2="20" y2="17" stroke="#fff"/><line x1="15" y1="20" x2="20" y2="20" stroke="#fff"/></svg>
    <span>Request For Quote</span>
  </div>
  <div class="quote-field" style="top:43px;height:28px">Name</div>
  <div class="quote-field" style="top:76px;height:28px">Email</div>
  <div class="quote-field" style="top:109px;height:63px">Write Your Message Here...</div>
  <div class="quote-submit">Submit</div>
</div>

<svg class="abs footer-shape" width="1167" height="130" aria-hidden="true">
  <polygon points="0,29 839,29 761,130 0,130" fill="var(--navy)"/>
  <polygon points="862,0 1167,0 1167,130 761,130" fill="#e6e6e6"/>
  <polyline points="862,0 761,130" stroke="#ffffff" stroke-width="3" fill="none"/>
</svg>
<div class="abs foot-links">Home<span class="sep">|</span>About Us<span class="sep">|</span>Mortgage Tools<span class="sep">|</span>How it Works<span class="sep">|</span>Contact Us</div>
<div class="abs foot-copy"><strong>©2013 Bramley Remates. Privacy Policy -</strong><br>Terms of Conditions. All Rights Reserved</div>
<div class="abs follow">FOLLOW US</div>
<div class="abs social" aria-label="Social links"><span></span><span></span><span></span><span></span></div>
<div class="abs foot-brand"><span class="brand-mark"></span><span class="brand-name">BRAMLEY</span></div>
</body>
</html>
```